Healthy lifestyle Influencer business card

I need your creativity to have a business card that I can leave in all the restaurants, hotels and spas I visit to inform them that I am an influencer specializing in the wellness sector and that I will write a review about them. You can use my instagram photos Lunavivo27 or on my website www.piattileggerisani.it. I would like my business card to impress with its creativity! thank you very much!

Contact Information for Business Card

siteweb, instagram, phone number

Font styles to use
Decorative
Script

Colors
0094D4
00A9DD
6FCCEA
C7EBF8
E9F6FB
59FF00
82FF00
B8FF75
E3FFCB
F4FFEA
FFC000
F8CF3A
FAE287
FDF2CF
FEFAEE
F0912C
F2A743
F7CA91
FBE8D2
FDF5EE
EE7325
F08F49
F5BC92
FAE3D3
FDF4ED
EB3D1F
EC4F4E
F09395
F8D3D4
FCEDEE
E54698
E96AAD
F1A4CE
F9D9EA
FCEFF6

Requirements
Nice to have
• creativity

```html
<!DOCTYPE html>
<html lang="it">
<head>
<meta charset="utf-8">
<title>Luna Vivo Chef – Biglietto da visita</title>
<link rel="stylesheet" href="https://fonts.googleapis.com/css2?family=Montserrat:wght@400;600;700&display=swap">
<style>
  :root {
    --stage: #1e1e1e;
    --card-front: #666666;
    --card-back: #ffffff;
    --ink: #4a4a4a;
    --ink-light: #f2f2f2;
    --peach: #f2dcc3;
    --peach-soft: #f8ebdd;
    --accent: #f2a743;
  }
  * { box-sizing: border-box; margin: 0; padding: 0; }
  html, body {
    width: 1200px; height: 800px; overflow: hidden;
    background: var(--stage);
    font-family: "Montserrat", sans-serif;
  }
  .canvas {
    position: relative; width: 1200px; height: 800px;
    display: flex; align-items: center; justify-content: center; gap: 40px;
  }
  .card {
    position: relative; width: 530px; height: 303px; overflow: hidden;
  }
  .card--front {
    background: var(--card-front);
    display: flex; align-items: center; justify-content: center;
  }
  .brand-name {
    font-weight: 400; font-size: 34px; letter-spacing: 1px;
  }
  .card--front .brand-name { color: var(--ink-light); }
  .card--back { background: var(--card-back); }
  .card--back .brand-name {
    position: absolute; left: 40px; top: 58px;
    color: var(--ink); font-size: 28px;
  }
  .swoosh { position: absolute; left: 0; bottom: 0; width: 530px; height: 120px; }
  .contact {
    position: absolute; left: 40px; top: 150px;
    color: var(--ink); font-size: 11.5px; line-height: 1.5;
    list-style: none;
  }
  .contact__address { margin-bottom: 6px; }
  .contact__item { display: flex; align-items: center; gap: 8px; }
  .contact__icon { width: 11px; height: 11px; flex: none; }
  .person {
    position: absolute; right: 40px; top: 118px; text-align: right;
  }
  .person__name {
    font-weight: 700; font-size: 19px; color: var(--ink); letter-spacing: 0.5px;
  }
  .person__role {
    font-size: 12px; color: var(--accent); margin-top: 2px;
  }
</style>
</head>
<body>
<main class="canvas">
  <section class="card card--front">
    <p class="brand-name">Luna Vivo Chef</p>
  </section>

  <section class="card card--back">
    <p class="brand-name">Luna Vivo Chef</p>

    <ul class="contact">
      <li class="contact__address">12 Via dei Tigli<br>Verona 37121</li>
      <li class="contact__item">
        <svg class="contact__icon" viewBox="0 0 12 12"><path d="M2.5 1 L4.5 1 L5.2 3.6 L4 4.6 Q5.2 7 7.4 8 L8.4 6.8 L11 7.5 L11 9.5 Q10.5 11 9 11 Q1 10 1 2.5 Q1 1 2.5 1 Z" fill="var(--accent)"/></svg>
        045.210.3381
      </li>
      <li class="contact__item">
        <svg class="contact__icon" viewBox="0 0 12 12"><rect x="0.5" y="2.5" width="11" height="7.5" fill="var(--accent)"/><path d="M0.8 2.8 L6 6.8 L11.2 2.8" stroke="#fff" stroke-width="1" fill="none"/></svg>
        info@piattileggerisani.it
      </li>
      <li class="contact__item">
        <svg class="contact__icon" viewBox="0 0 12 12"><circle cx="6" cy="6" r="5" fill="none" stroke="var(--accent)" stroke-width="1.2"/><ellipse cx="6" cy="6" rx="2.2" ry="5" fill="none" stroke="var(--accent)" stroke-width="1"/><path d="M1 6 H11" stroke="var(--accent)" stroke-width="1"/></svg>
        www.piattileggerisani.it
      </li>
      <li class="contact__item">
        <svg class="contact__icon" viewBox="0 0 12 12"><circle cx="6" cy="6" r="5" fill="none" stroke="var(--accent)" stroke-width="1.4"/></svg>
        @lunavivo27
      </li>
    </ul>

    <div class="person">
      <p class="person__name">GIULIA FERRI</p>
      <p class="person__role">President</p>
    </div>

    <svg class="swoosh" viewBox="0 0 530 120" preserveAspectRatio="none">
      <path d="M0 95 Q260 95 530 15 L530 120 L0 120 Z" fill="var(--peach)"/>
      <path d="M120 92 Q330 78 530 28" stroke="var(--peach-soft)" stroke-width="3" fill="none"/>
      <path d="M200 88 Q380 70 530 38" stroke="#ffffff" stroke-width="2" fill="none"/>
    </svg>
  </section>
</main>
</body>
</html>
```